Pinecrest Lockworks Business Card Design

Double Sided Business Card Design for a Locksmith company specializing in Safecracking, safe & vault service.

```html
<!DOCTYPE html>
<html lang="en">
<head>
<meta charset="utf-8">
<title>Pinecrest Lockworks – Business Card</title>
<link rel="stylesheet" href="https://fonts.googleapis.com/css2?family=Archivo+Black&family=Arimo:wght@400;700&display=swap">
<style>
  :root {
    --brand-green: #337c3c;
    --brand-green-tint: #e9f0ea;
    --ink: #1b1b1b;
    --ink-soft: #555555;
    --paper: #ffffff;
    --stage: #2f2f2f;
    --rule: #cfcfcf;
  }
  * { box-sizing: border-box; margin: 0; padding: 0; }
  html, body { width: 1200px; height: 866px; overflow: hidden; }
  body {
    background: var(--stage);
    font-family: "Arimo", Arial, sans-serif;
    color: var(--ink);
    display: flex;
    flex-direction: column;
    align-items: center;
    justify-content: center;
    gap: 40px;
  }
  .card {
    position: relative;
    width: 600px;
    height: 343px;
    overflow: hidden;
  }
  .card--front { background: var(--paper); }
  .card--back { background: var(--brand-green); }

  .card__backdrop {
    position: absolute;
    left: 40px;
    top: -30px;
    width: 300px;
    height: 300px;
    border-radius: 50%;
    background: var(--brand-green-tint);
  }

  .contact {
    position: absolute;
    left: 34px;
    top: 46px;
  }
  .contact__name {
    font-family: "Archivo Black", Arial, sans-serif;
    font-size: 20px;
    letter-spacing: 0.5px;
    color: var(--brand-green);
    text-transform: uppercase;
  }
  .contact__role {
    font-size: 11px;
    letter-spacing: 1.2px;
    color: var(--ink-soft);
    text-transform: uppercase;
    margin: 3px 0 12px;
  }
  .contact__list { list-style: none; }
  .contact__item {
    display: flex;
    align-items: center;
    gap: 8px;
    font-size: 12.5px;
    line-height: 19px;
    letter-spacing: 0.3px;
  }
  .contact__item svg { width: 12px; height: 12px; fill: var(--brand-green); flex: none; }
  .contact__item .accent { color: var(--brand-green); }

  .wordmark {
    position: absolute;
    display: flex;
    align-items: center;
    gap: 14px;
  }
  .wordmark__dot {
    width: 64px;
    height: 64px;
    border-radius: 50%;
    background: var(--brand-green);
    flex: none;
  }
  .wordmark__name {
    font-family: "Archivo Black", Arial, sans-serif;
    text-transform: uppercase;
    line-height: 1;
  }
  .card--front .wordmark { left: 300px; top: 92px; }
  .card--front .wordmark__name { font-size: 24px; color: var(--ink); letter-spacing: 1px; }

  .card__rule {
    position: absolute;
    left: 280px;
    right: 40px;
    top: 222px;
    border-top: 1px solid var(--rule);
  }
  .address {
    position: absolute;
    right: 40px;
    top: 240px;
    text-align: right;
    font-size: 13px;
    line-height: 19px;
    letter-spacing: 0.5px;
    color: var(--ink);
  }

  .card--back .wordmark { left: 50%; top: 50%; transform: translate(-50%, -50%); gap: 18px; }
  .card--back .wordmark__dot { background: var(--paper); width: 76px; height: 76px; }
  .card--back .wordmark__name { font-size: 30px; color: var(--paper); letter-spacing: 1.5px; }
</style>
</head>
<body>

<section class="card card--front">
  <div class="card__backdrop"></div>

  <div class="contact">
    <h1 class="contact__name">Daniel Harper</h1>
    <p class="contact__role">Managing Director</p>
    <ul class="contact__list">
      <li class="contact__item">
        <svg viewBox="0 0 24 24" aria-hidden="true"><path d="M6.6 10.8a15 15 0 0 0 6.6 6.6l2.2-2.2a1 1 0 0 1 1-.25 11.4 11.4 0 0 0 3.6.57 1 1 0 0 1 1 1V20a1 1 0 0 1-1 1A17 17 0 0 1 3 4a1 1 0 0 1 1-1h3.5a1 1 0 0 1 1 1c0 1.25.2 2.45.57 3.57a1 1 0 0 1-.25 1z"/></svg>
        055-310 274 618
      </li>
      <li class="contact__item">
        <svg viewBox="0 0 24 24" aria-hidden="true"><path d="M6 2h12v6H6zM3 9h18a1 1 0 0 1 1 1v7h-4v5H6v-5H2v-7a1 1 0 0 1 1-1zm5 7v4h8v-4z"/></svg>
        055-310 274 618
      </li>
      <li class="contact__item">
        <svg viewBox="0 0 24 24" aria-hidden="true"><path d="M2 5h20v14H2zm2 2v.5l8 5 8-5V7z"/></svg>
        info@pinecrestlock.com
      </li>
      <li class="contact__item">
        <svg viewBox="0 0 24 24" aria-hidden="true"><path d="M12 2a10 10 0 1 0 0 20 10 10 0 0 0 0-20zm1 2.1c1.3.9 2.3 3 2.6 5.9H13zm-2 0V10H8.4c.3-2.9 1.3-5 2.6-5.9zM4.1 12h4.3c0 2 .4 3.8 1 5.1A8 8 0 0 1 4.1 12zm6.9 7.9c-1.3-.9-2.4-3.2-2.6-5.9H11zm2 0V14h2.6c-.2 2.7-1.3 5-2.6 5.9zm1.6-2.8c.6-1.3 1-3.1 1-5.1h4.3a8 8 0 0 1-5.3 5.1z"/></svg>
        <span>www.<span class="accent">pinecrestlock</span>.com</span>
      </li>
    </ul>
  </div>

  <div class="wordmark">
    <span class="wordmark__dot"></span>
    <span class="wordmark__name">Pinecrest<br>Lockworks</span>
  </div>

  <div class="card__rule"></div>

  <address class="address">
    421, Address line goes here<br>
    45452, Country Name
  </address>
</section>

<section class="card card--back">
  <div class="wordmark">
    <span class="wordmark__dot"></span>
    <span class="wordmark__name">Pinecrest<br>Lockworks</span>
  </div>
</section>

</body>
</html>
```